Minimalist Sign Design (24” X 24”)

I am wanting to redesign our yard signs to be very clean, attractive, eye catching, and readable (imagine driving by a home with a sign In yard). We paint homes. I am hoping to have a design that incorporates our brand colors in a clean, professional way that represents our company. Clean, concise, easily read from a distance.

Target Market(s)

Homeowners

Industry/Entity Type

Painting And Decorating

Font styles to use
Sans Serif

Requirements
Must have
• Phone Number: (555) 014-7391
• Free Consultations
• Makeover in progress!
• Brand colors:
• Hunter Green: #355e3b
• Black
• White
Nice to have
• Would like the hunter green to he background color of sign. Can make logo white to stand out with the green.
Should not have
• Too busy or unable to read text

```html
<!DOCTYPE html>
<html lang="en">
<head>
<meta charset="utf-8">
<title>Minimalist Sign Design – Meridian Painting</title>
<link href="https://fonts.googleapis.com/css2?family=Poppins:wght@400&family=Rubik:wght@500;700;800&display=swap" rel="stylesheet">
<style>
  :root {
    --stage: #667a7a;
    --hunter: #276a1b;
    --ink: #070908;
    --paper: #ffffff;
  }
  * { margin: 0; padding: 0; box-sizing: border-box; }
  html, body { width: 1200px; height: 740px; overflow: hidden; background: var(--stage); }
  .board { position: relative; width: 1200px; height: 740px; font-family: "Rubik", sans-serif; }

  .board-title {
    position: absolute; top: 40px; left: 0; width: 100%;
    text-align: center; font: 400 30px/1 "Poppins", sans-serif; color: var(--paper);
  }
  .sample-label {
    position: absolute; top: 652px;
    font: 400 27px/1 "Poppins", sans-serif; color: var(--paper);
  }

  .sign {
    position: absolute; top: 118px; width: 503px; height: 503px; overflow: hidden;
    box-shadow: 0 2px 6px rgba(0,0,0,.35);
  }
  .sign--green { left: 75px; background: var(--hunter); }
  .sign--split { left: 626px; background: var(--paper); }

  .band { position: absolute; left: 0; width: 100%; }
  .sign--green .band--tagline { top: 363px; height: 57px; background: var(--ink); }
  .sign--green .band--contact { top: 420px; height: 83px; background: var(--paper); }
  .sign--split .band--headline { top: 198px; height: 162px; background: var(--ink); }
  .sign--split .band--tagline { top: 360px; height: 62px; background: var(--hunter); }
  .sign--split .band--contact { top: 422px; height: 81px; background: var(--paper); }

  .brand-tab {
    position: absolute; left: 163px; top: 0; width: 177px; height: 191px;
    background: var(--hunter); border-radius: 0 0 88.5px 88.5px;
  }

  .brand-name {
    position: absolute; left: 0; width: 100%; text-align: center;
    font-weight: 500; color: var(--paper); line-height: 1.15; letter-spacing: .12em;
  }
  .sign--green .brand-name { top: 78px; font-size: 24px; }
  .sign--split .brand-name { top: 82px; font-size: 19px; }

  .headline-free, .headline-sub, .tagline, .phone {
    position: absolute; left: 0; width: 100%; text-align: center; line-height: 1; white-space: nowrap;
  }
  .headline-free { font-weight: 800; font-size: 123px; color: var(--paper); letter-spacing: .01em; }
  .headline-sub { font-weight: 800; font-size: 47px; color: var(--paper); }
  .sign--green .headline-free { top: 195px; }
  .sign--green .headline-sub { top: 307px; }
  .sign--split .headline-free { top: 189px; }
  .sign--split .headline-sub { top: 302px; }

  .tagline {
    display: flex; justify-content: center; align-items: center;
    font-weight: 500; font-size: 34px; color: var(--paper);
  }
  .sign--green .tagline { top: 363px; height: 57px; }
  .sign--split .tagline { top: 360px; height: 62px; }

  .phone {
    display: flex; justify-content: center; align-items: center; gap: 10px;
    font-weight: 800; font-size: 52px; letter-spacing: -0.01em; color: var(--ink);
  }
  .sign--green .phone { top: 420px; height: 83px; }
  .sign--split .phone { top: 422px; height: 81px; }
  .phone-icon { width: 46px; height: 46px; flex: none; }
</style>
</head>
<body>
<main class="board">
  <h1 class="board-title">Minimalist Sign Design (24” X 24”)</h1>

  <section class="sign sign--green" aria-label="Sign option one">
    <div class="brand-name">MERIDIAN<br>PAINTING</div>
    <div class="headline-free">FREE</div>
    <div class="headline-sub">CONSULTATIONS</div>
    <div class="band band--tagline"></div>
    <div class="tagline">MAKEOVER IN PROGRESS!</div>
    <div class="band band--contact"></div>
    <div class="phone">
      <svg class="phone-icon" viewBox="0 0 46 46" aria-hidden="true">
        <circle cx="23" cy="23" r="23" fill="var(--hunter)"/>
        <path d="M22 12c-4 1-6 5-6 11s2 10 6 11l2-1-1-6-2-0.5c-.7-1.5-.7-5.5 0-7l2-.5 1-6z" fill="var(--paper)"/>
      </svg>
      <span>(555) 014-7391</span>
    </div>
  </section>

  <section class="sign sign--split" aria-label="Sign option two">
    <div class="brand-tab"></div>
    <div class="brand-name">MERIDIAN<br>PAINTING</div>
    <div class="band band--headline"></div>
    <div class="headline-free">FREE</div>
    <div class="headline-sub">CONSULTATIONS</div>
    <div class="band band--tagline"></div>
    <div class="tagline">MAKEOVER IN PROGRESS!</div>
    <div class="band band--contact"></div>
    <div class="phone">
      <svg class="phone-icon" viewBox="0 0 46 46" aria-hidden="true">
        <circle cx="23" cy="23" r="23" fill="var(--hunter)"/>
        <path d="M22 12c-4 1-6 5-6 11s2 10 6 11l2-1-1-6-2-0.5c-.7-1.5-.7-5.5 0-7l2-.5 1-6z" fill="var(--paper)"/>
      </svg>
      <span>(555) 014-7391</span>
    </div>
  </section>

  <p class="sample-label" style="left:75px">Sample 1</p>
  <p class="sample-label" style="left:626px">Sample 2</p>
</main>
</body>
</html>
```